electrical automation company needs a letterhead design

we need a letter head designed for our new electrical automation company. Our company color are orange and blue as you'll see from our logo attached

Target Market(s)

Domestic, commercial and industrial electrical clients

Industry/Entity Type

Electrical

Contact Information for Business Card

I need to update my business card to make it more eye catching I have attached my old business card designs, logo and new trifold brochure to give you an idea

Font styles to use
Sans Serif

Colors
f37122
0393ce

Requirements
Must have
• larkfield electrical logo
my name
phone number
email
website
Nice to have
• QR code linked to my website
list of some services
- domestic
- commercial
- industrial

```html
<!DOCTYPE html>
<html lang="en">
<head>
<meta charset="utf-8">
<title>Larkfield Electrical Letterhead</title>
<link href="https://fonts.googleapis.com/css2?family=Didact+Gothic&family=Lato:ital,wght@0,400;0,700;1,700&display=swap" rel="stylesheet">
<style>
  :root {
    --stage: #b9b9b9;
    --paper: #ffffff;
    --blue: #0a72bd;
    --band-blue: #3f77b2;
    --orange: #f05a33;
    --ink: #2b2b2b;
    --ink-soft: #555555;
    --name-red: #a3121a;
  }
  * { margin: 0; padding: 0; box-sizing: border-box; }
  html, body { width: 1082px; height: 1200px; overflow: hidden; background: var(--stage); }
  .letterhead {
    position: absolute; left: 142px; top: 73px; width: 798px; height: 1062px;
    background: var(--paper); overflow: hidden;
    font-family: "Didact Gothic", sans-serif; color: var(--ink);
  }
  .brand {
    position: absolute; left: 68px; top: 92px; display: flex; align-items: center; gap: 10px;
  }
  .brand-dot { width: 44px; height: 44px; border-radius: 50%; background: var(--orange); flex: none; }
  .brand-name { font-family: "Lato", sans-serif; font-weight: 700; font-size: 27px; color: var(--blue); white-space: nowrap; }
  .contact { position: absolute; left: 651px; top: 25px; font-family: "Lato", sans-serif; }
  .contact-address { color: var(--orange); font-size: 11px; line-height: 14px; }
  .contact-list {
    list-style: none; margin-top: 4px; margin-left: 1px; padding-left: 7px;
    border-left: 1px solid #e9b39a; font-size: 7.6px; color: var(--ink); line-height: 13.2px;
  }
  .contact-list li { display: flex; align-items: center; gap: 4px; }
  .contact-list svg { width: 8px; height: 8px; flex: none; }
  .recipient { position: absolute; left: 91px; top: 199px; }
  .recipient .label { font-family: "Lato", sans-serif; font-size: 14px; color: #000; }
  .recipient .name { margin-top: 13px; color: var(--name-red); font-size: 15px; line-height: 16px; }
  .recipient .role { font-size: 9.5px; color: var(--ink-soft); line-height: 11px; }
  .recipient .line { font-size: 15px; line-height: 17px; }
  .body-text { position: absolute; left: 91px; width: 640px; font-size: 14.4px; line-height: 17.2px; color: var(--ink); }
  .p1 { top: 332px; } .p2 { top: 436px; } .p3 { top: 521px; } .p4 { top: 677px; } .p5 { top: 763px; }
  .signoff { position: absolute; left: 91px; top: 848px; font-family: "Lato", sans-serif; font-style: italic; font-weight: 700; font-size: 13px; color: #000; }
  .footer-band {
    position: absolute; left: 0; top: 1009px; width: 700px; height: 47px;
    background: var(--band-blue); border-top: 2px solid var(--orange); border-bottom: 2px solid var(--orange);
    display: flex; align-items: center; justify-content: center; padding-right: 40px;
  }
  .footer-band .services { font-family: "Lato", sans-serif; color: #fff; font-size: 20px; }
  .footer-brand { position: absolute; left: 678px; top: 1022px; display: flex; align-items: center; gap: 4px; }
  .footer-brand .brand-dot { width: 18px; height: 18px; }
  .footer-brand .brand-name { font-size: 10.5px; }
</style>
</head>
<body>
  <main class="letterhead">
    <div class="brand">
      <span class="brand-dot"></span>
      <span class="brand-name">Larkfield Electrical</span>
    </div>

    <div class="contact">
      <p class="contact-address">2140harbour view<br>&nbsp;sa 5710</p>
      <ul class="contact-list">
        <li><svg viewBox="0 0 10 10"><circle cx="5" cy="5" r="4.5" fill="var(--blue)"/><path d="M3.2 2.6l1 1-0.6 0.7a3.5 3.5 0 0 0 2.1 2.1l0.7-0.6 1 1-0.8 0.8C4.8 7.4 2.6 5.2 2.4 3.4z" fill="#fff"/></svg>0491570156</li>
        <li><svg viewBox="0 0 10 10"><rect x="0.5" y="2" width="9" height="6" fill="none" stroke="var(--blue)" stroke-width="0.8"/><path d="M0.5 2l4.5 3.5L9.5 2" fill="none" stroke="var(--blue)" stroke-width="0.8"/></svg>hello@larkfieldelectrical.com</li>
        <li><svg viewBox="0 0 10 10"><circle cx="5" cy="5" r="4.5" fill="var(--blue)"/><path d="M0.5 5h9M5 0.5c-2 2.5-2 6.5 0 9M5 0.5c2 2.5 2 6.5 0 9" fill="none" stroke="#fff" stroke-width="0.6"/></svg>www.larkfieldelectrical.com</li>
      </ul>
    </div>

    <section class="recipient">
      <p class="label">TO</p>
      <p class="name">HARLOW</p>
      <p class="role">Director</p>
      <p class="line">Design Studio</p>
      <p class="line">A: 172 430 618</p>
      <p class="line">B:8264&nbsp; 913 302</p>
    </section>

    <p class="body-text p1">Lorem ipsum dolor sit amet, consectetur adipiscing elit. Vestibulum consectetur egestas metus, quis scelerisque tortor consectetur sed. Nullam sit amet lorem sed arcu faucibus semper. Vestibulum ante ipsum primis in faucibus orci luctus et ultrices posuere cubilia Curae; Sed sagittis arcu ut ligula molestie malesuada. Suspendisse posuere tincidunt elit, at ullamcorper augue blandit vitae.</p>
    <p class="body-text p2">Cras egestas vestibulum pulvinar. Donec iaculis imperdiet hendrerit. Sed mollis, enim quis hendrerit dictum, tortor mauris vulputate ligula, viverra porta magna libero at mi. Integer odio nisl, luctus nec dui in, rutrum sollicitudin nisi. Suspendisse nec erat eros.</p>
    <p class="body-text p3">Sed dictum quam arcu, sit amet ullamcorper orci faucibus eget. Morbi finibus ante at risus commodo, nec ullamcorper nulla tincidunt. Integer eu molestie nulla, sed consequat tortor. Sed ullamcorper congue metus, vitae dictum nibh luctus sed. Suspendisse ornare purus fermentum, viverra elit sed, bibendum ex. Vivamus semper diam vel diam laoreet rutrum. Ut porta fermentum velit. Vestibulum vitae semper nisl. Sed facilisis at ex et vestibulum. Donec at magna ut eros pulvinar hendrerit.</p>
    <p class="body-text p4">Sed dictum quam arcu, sit amet ullamcorper orci faucibus eget. Morbi finibus ante at risus commodo, nec ullamcorper nulla tincidunt. Integer eu molestie nulla, sed consequat tortor. Sed ullamcorper congue metus, vitae dictum nibh luctus sed. Suspendisse ornare purus fermentum, viverra elit sed, bibendum ex.</p>
    <p class="body-text p5">Vivamus semper diam vel diam laoreet rutrum. Ut porta fermentum velit. Vestibulum vitae semper nisl. Sed facilisis at ex et vestibulum. Donec at magna ut eros pulvinar hendrerit.</p>

    <p class="signoff">Regards,</p>

    <footer class="footer-band">
      <span class="services">domestic- commercial- industrial</span>
    </footer>
    <div class="footer-brand">
      <span class="brand-dot"></span>
      <span class="brand-name">Larkfield Electrical</span>
    </div>
  </main>
</body>
</html>
```